Website for Bramblewood Quarry Advisors

Please design a website that initially contains four or five pages. This work is for a newly formed consulting company, Bramblewood Quarry Advisors, that provides training and individual coaching to help business professionals and lawyers write more effectively and efficiently.

We work in a professional and conservative industry. The website should be simple, crisp, and clean.

I have attached a document that describes the four initial pages for the site: 1) a landing page, 2) a webpage that includes the pictures and bios of our two consultants, 3) a webpage that describes our services, and 4) a webpage that will contain a form that visitors can use to submit questions to us.

I also included the following files:
a. a powerpoint slide with our consultants' pictures and bios; and
b. our recently designed logo (jpg and png files).

Thank you!

```html
<!DOCTYPE html>
<html lang="en">
<head>
<meta charset="utf-8">
<title>Bramblewood Quarry Advisors</title>
<link rel="stylesheet" href="https://fonts.googleapis.com/css2?family=Crimson+Pro:wght@400;500&family=Poppins:wght@400;500&display=swap">
<style>
:root{
  --red:#c8262c;
  --ink:#111111;
  --text:#2b2b2b;
  --grey-band:#ededed;
  --bracket-grey:#6f6f6f;
  --line:#d6d6d6;
  --white:#ffffff;
  --serif:"Crimson Pro", Georgia, serif;
  --sans:"Poppins", Arial, sans-serif;
}
*{margin:0;padding:0;box-sizing:border-box}
html,body{width:1200px;height:3411px;overflow:hidden}
body{position:relative;background:var(--white);color:var(--text);font-family:var(--sans)}
.btn{position:absolute;display:flex;align-items:center;justify-content:center;background:var(--red);color:var(--white);font-family:var(--serif);font-size:21px;width:164px;height:54px;text-decoration:none}
.section-title{position:absolute;left:0;width:1200px;text-align:center;font-family:var(--serif);font-weight:400;color:var(--ink);font-size:44px;line-height:1}

/* header */
.site-header{position:absolute;top:0;left:0;width:1200px;height:80px;background:var(--white)}
.brand{position:absolute;left:75px;top:28px;font-family:var(--serif);font-size:21px;color:var(--ink);white-space:nowrap}
.main-nav{position:absolute;right:72px;top:30px;display:flex;gap:47px;font-family:var(--serif);font-size:20px}
.main-nav a{color:var(--ink);text-decoration:none}
.main-nav a.active{color:var(--red)}

/* hero */
.hero{position:absolute;top:80px;left:0;width:1200px;height:658px;background:linear-gradient(90deg,#f7f7f7 0%,#f2f2f2 40%,#e6e6e6 100%)}
.hero-photo{position:absolute;left:380px;top:0;width:820px;height:658px;background:linear-gradient(90deg,rgba(240,240,240,0) 0%,#dcdcdc 25%,#b9b6b3 55%,#8d94a3 80%,#c9ccd1 100%)}
.hero-title{position:absolute;left:75px;top:170px;font-family:var(--serif);font-weight:400;font-size:54px;line-height:50px;color:var(--ink)}
.hero-text{position:absolute;left:75px;top:312px;width:520px;font-size:18px;line-height:30px;color:var(--text)}

/* welcome */
.welcome-bracket-red{position:absolute;left:60px;top:808px;width:76px;height:424px;border-left:14px solid var(--red);border-top:14px solid var(--red)}
.welcome-bracket-grey{position:absolute;left:524px;top:1159px;width:77px;height:106px;border-right:12px solid var(--bracket-grey);border-bottom:12px solid var(--bracket-grey)}
.welcome-photo{position:absolute;left:75px;top:825px;width:512px;height:425px;background:linear-gradient(135deg,#d9dbdd 0%,#a7a9ac 35%,#3e4552 65%,#c8c2ba 100%)}
.welcome-title{position:absolute;left:617px;top:836px;font-family:var(--serif);font-weight:400;font-size:41px;line-height:43px;color:var(--ink)}
.welcome-text{position:absolute;left:616px;top:960px;width:495px;font-size:15px;line-height:28px}

/* consultants */
.consultants{position:absolute;top:1338px;left:0;width:1200px;height:657px;background:var(--grey-band)}
.bracket-grey-left{position:absolute;left:60px;top:1830px;width:76px;height:106px;border-left:13px solid var(--bracket-grey);border-bottom:13px solid var(--bracket-grey)}
.bracket-grey-right{position:absolute;left:1063px;top:1527px;width:77px;height:106px;border-right:13px solid var(--bracket-grey);border-top:13px solid var(--bracket-grey)}
.consultant-card{position:absolute;top:1542px;width:512px;height:379px;background:var(--white);text-align:center}
.avatar{position:absolute;top:1485px;width:114px;height:114px;border-radius:50%}
.consultant-name{position:absolute;top:76px;left:0;width:100%;font-family:var(--serif);font-size:27px;font-weight:400;color:var(--red)}
.consultant-bio{position:absolute;top:116px;left:28px;right:28px;font-size:13.3px;line-height:25.6px}
.consultant-card .btn{left:174px;top:291px}

/* services */
.services-intro{position:absolute;left:100px;top:2133px;width:1000px;text-align:center;font-size:15.5px;line-height:28px}
.service-box{position:absolute;top:2220px;width:242px;height:375px;border:1px solid var(--line);text-align:center;background:var(--white)}
.service-icon{position:absolute;left:86px;top:20px;width:70px;height:70px;background:#e9e9e9}
.service-title{position:absolute;left:14px;right:14px;top:110px;font-family:var(--serif);font-size:22px;line-height:26px;font-weight:400;color:var(--red)}
.service-text{font-size:13.3px;line-height:24px;padding:0 14px;position:absolute;left:0;right:0}

/* contact */
.contact{position:absolute;top:2666px;left:0;width:1200px;height:490px;background:linear-gradient(120deg,#4a413c 0%,#2f2824 35%,#3a312b 60%,#1e1a18 100%)}
.contact .section-title{color:var(--white)}
.contact-sub{position:absolute;top:138px;left:0;width:1200px;text-align:center;color:var(--white);font-size:15px}
.field{position:absolute;width:431px;height:51px;background:var(--white);font-size:13.5px;color:var(--ink);padding-left:9px;display:flex;align-items:center}

/* footer */
.footer-brand{position:absolute;left:0;top:3190px;width:1200px;text-align:center;font-family:var(--serif);font-size:31px;color:var(--ink)}
.footer-nav{position:absolute;left:0;top:3266px;width:1200px;display:flex;justify-content:center;gap:47px;font-family:var(--serif);font-size:20px}
.footer-nav a{color:var(--ink);text-decoration:none}
.copyright{position:absolute;left:0;top:3303px;width:1200px;text-align:center;font-size:12.5px;color:var(--ink)}
.social{position:absolute;left:0;top:3344px;width:1200px;display:flex;justify-content:center;gap:20px}
.social span{width:22px;height:22px;border-radius:50%;background:var(--red);display:block}
</style>
</head>
<body>

<header class="site-header">
  <div class="brand">Bramblewood Quarry Advisors</div>
  <nav class="main-nav">
    <a class="active" href="#">Home</a>
    <a href="#">About Us</a>
    <a href="#">Consultants</a>
    <a href="#">Services</a>
    <a href="#">Contact Us</a>
  </nav>
</header>

<section class="hero">
  <div class="hero-photo" role="img" aria-label="Photo of a consultant coaching a colleague at a laptop in a bright office"></div>
  <h1 class="hero-title">Bramblewood Quarry<br>Advisors</h1>
  <p class="hero-text">We provides training and individual coaching to help business professionals and lawyers write more effectively and efficiently.</p>
  <a class="btn" style="left:75px;top:422px" href="#">Read More</a>
</section>

<section class="welcome">
  <div class="welcome-bracket-red"></div>
  <div class="welcome-bracket-grey"></div>
  <div class="welcome-photo" role="img" aria-label="Photo of two businessmen reviewing work on a tablet"></div>
  <h2 class="welcome-title">Welcome to Bramblewood<br>Quarry Advisors</h2>
  <p class="welcome-text">We train and coach business professionals and lawyers on strategies and techniques to engage, inform, and persuade their readers. We teach our clients that precisely understanding their readers’ concerns and motivations leads them to select the appropriate tone, to develop the most effective narrative, and to make the complicated judgments necessary for effective written communication.</p>
  <a class="btn" style="left:616px;top:1179px" href="#">Read More</a>
</section>

<section class="consultants">
  <h2 class="section-title" style="top:70px">Consultants</h2>
</section>
<div class="bracket-grey-left"></div>
<div class="bracket-grey-right"></div>

<article class="consultant-card" style="left:75px">
  <h3 class="consultant-name">Marta Ellingsworth</h3>
  <p class="consultant-bio">Marta Ellingsworth is an Associate Professor and Director of the Academic Enrichment Program at Harwick University School of Law. She has devoted her career in legal education to teaching and counseling students and attorneys, with a focus on developing the fundamental skills to promote success and wellbeing in law school and in the legal profession.</p>
  <a class="btn" href="#">Read More</a>
</article>
<div class="avatar" style="left:274px;background:linear-gradient(160deg,#b7a58a,#6f7c88)" role="img" aria-label="Portrait photo of Marta Ellingsworth"></div>

<article class="consultant-card" style="left:615px">
  <h3 class="consultant-name">Dorian Kettleby</h3>
  <p class="consultant-bio">Dorian Kettleby provides legal and business writing consulting services to businesses, business professionals, law firms, and attorneys. He earned a Bachelor of Arts, cum laude, in English from Ashgrove University, a Master of Fine Arts in creative writing from the Linden Valley Writers’ Workshop, and a Juris Doctor, cum laude, from Carrow Law School.</p>
  <a class="btn" href="#">Read More</a>
</article>
<div class="avatar" style="left:814px;background:linear-gradient(160deg,#8c7b6d,#5a4538)" role="img" aria-label="Portrait photo of Dorian Kettleby"></div>

<section class="services">
  <h2 class="section-title" style="top:2043px">Our Services</h2>
  <p class="services-intro">The list below presents an overview of our services. We take pride in ensuring that our work connects with each client’s unique characteristics and its culture for written communications.</p>

  <div class="service-box" style="left:75px">
    <div class="service-icon" role="img" aria-label="Line icon of a large group training session"></div>
    <h3 class="service-title">Training for twenty or more professionals</h3>
    <p class="service-text" style="top:178px">Nemo enim ipsam voluptatem quia voluptas sit aspernatur aut odit aut fugit, sed quia consequuntur magni dolores eos qui ratione aute irure dolor in reprehenderit in voluptate velit esse cillum dolore.</p>
  </div>
  <div class="service-box" style="left:344px">
    <div class="service-icon" role="img" aria-label="Line icon of a cohort in front of a presentation chart"></div>
    <h3 class="service-title">Training for cohorts of up to twenty professionals</h3>
    <p class="service-text" style="top:204px">Nemo enim ipsam voluptatem quia voluptas sit aspernatur aut odit aut fugit, sed quia consequuntur magni aute irure dolor in reprehenderit in voluptate velit esse.</p>
  </div>
  <div class="service-box" style="left:615px">
    <div class="service-icon" role="img" aria-label="Line icon of a professional with a briefcase"></div>
    <h3 class="service-title">Training for cohorts followed by one-hour individual coaching for each participant</h3>
    <p class="service-text" style="top:230px">Nemo enim ipsam voluptatem quia voluptas sit aspernatur aut odit aut fugit, sed quia consequuntur magni dolores eos qui ratione.</p>
  </div>
  <div class="service-box" style="left:885px">
    <div class="service-icon" role="img" aria-label="Line icon of two people in a one-on-one conversation"></div>
    <h3 class="service-title">Individual<br>coaching</h3>
    <p class="service-text" style="top:178px">Nemo enim ipsam voluptatem quia voluptas sit aspernatur aut odit aut fugit, sed quia consequuntur magni dolores eos qui ratione aute irure dolor in reprehenderit in voluptate velit esse cillum dolore.</p>
  </div>
</section>

<section class="contact" role="img" aria-label="Dark background photo of hands writing at a desk">
  <h2 class="section-title" style="top:62px">Contact Us</h2>
  <p class="contact-sub">Include a page for visitors to complete a form and submit and email to us</p>
  <div class="field" style="left:164px;top:176px">Company name</div>
  <div class="field" style="left:609px;top:176px">Email address</div>
  <div class="field" style="left:164px;top:240px">Contact name</div>
  <div class="field" style="left:609px;top:240px">Physical address</div>
  <div class="field" style="left:164px;top:304px">Contact phone number</div>
  <div class="field" style="left:609px;top:304px">Open field</div>
  <a class="btn" style="left:518px;top:370px" href="#">Submit</a>
</section>

<footer>
  <div class="footer-brand">Bramblewood Quarry Advisors</div>
  <nav class="footer-nav">
    <a href="#">Home</a><a href="#">About Us</a><a href="#">Consultants</a><a href="#">Services</a><a href="#">Contact Us</a>
  </nav>
  <p class="copyright">Copyrights© 2024 Company Name All Rights Reserved</p>
  <div class="social">
    <span aria-label="Social link 1"></span><span aria-label="Social link 2"></span><span aria-label="Social link 3"></span><span aria-label="Social link 4"></span><span aria-label="Social link 5"></span>
  </div>
</footer>

</body>
</html>
```